Food Safety Consultancy Flyer Design

We need a flyer design for a new company called KLS Training. New food safety regulations are coming into effect for all food operators in March 2016. My company provides training and resources to support food operators during the transition onto the new Kitchen Ledger Scheme. For the designs we would like to see any of the colours used from the logo which is attached. The flyer will be letting operators know that there are new regulations and we are here to help. Our company offers three packages: 1. Videos (training videos) 2. Webinars and Workshop 3. One-on-one mentoring. Our websites main colour used is the green colour from the logo.
Food service operators: cafes, restaurants etc.
Hospitality

```html
<!DOCTYPE html>
<html lang="en">
<head>
<meta charset="utf-8">
<title>KLS Training – Food Act 2014 Flyer</title>
<link href="https://fonts.googleapis.com/css2?family=Jost:wght@400;500;700&family=Exo+2:ital,wght@1,900&display=swap" rel="stylesheet">
<style>
  :root{
    --green:#3aaa47;
    --orange:#f7a83b;
    --blue:#2270b8;
    --ink:#2b2b2b;
    --paper:#f4f4f4;
    --stage:#e4e5e7;
  }
  *{margin:0;padding:0;box-sizing:border-box}
  html,body{width:1194px;height:1200px;overflow:hidden}
  body{background:var(--stage);font-family:"Jost",sans-serif;color:var(--ink);position:relative}
  .flyer{position:absolute;left:175px;top:0;width:844px;height:1200px}
  .frame{position:absolute;inset:0}
  .sheet{position:absolute;left:28px;top:28px;width:788px;height:1144px;
    background:radial-gradient(ellipse at 50% 40%,#fbfbfb 0%,#ececec 60%,#dcdcdc 100%);overflow:hidden}
  .chef-art{position:absolute;left:82px;top:-8px;width:580px;height:250px;border-radius:40px 40px 0 0;
    background:linear-gradient(180deg,#ffffff 0%,#f1f1f1 40%,#f3b46a 100%)}
  .headline-disc{position:absolute;left:0;top:0}
  .headline{position:absolute;left:0;width:788px;top:286px;text-align:center;
    font-family:"Exo 2",sans-serif;font-style:italic;font-weight:900;font-size:40px;line-height:41px;
    color:#fff;text-transform:uppercase;letter-spacing:-0.5px;
    text-shadow:2px 2px 0 #1f2a44,-1px -1px 0 #1f2a44,1px -1px 0 #1f2a44,-1px 1px 0 #1f2a44,3px 4px 0 #1f2a44}
  .intro{position:absolute;left:0;width:788px;top:469px;text-align:center;font-size:21px;line-height:30.5px}
  .bar{position:absolute;left:66px;width:656px;height:23px;background:var(--blue);color:#fff;
    font-weight:700;text-align:center;font-size:17px;line-height:23px;letter-spacing:2.5px}
  .bar.tagline{top:569px}
  .bar.packages{top:729px;letter-spacing:21px;font-size:16px}
  .knowledge{position:absolute;left:0;width:788px;top:601px;text-align:center;font-size:17px;line-height:26px}
  .knowledge strong{font-weight:700}
  .rule{position:absolute;left:71px;width:645px;top:686px;height:2px;background:var(--green)}
  .help{position:absolute;left:0;width:788px;top:694px;text-align:center;font-size:16px}
  .package{position:absolute;top:772px;text-align:center;font-size:15.5px;line-height:22px}
  .package h3{font-size:17px;font-weight:700;text-transform:uppercase;line-height:20px;margin-bottom:3px}
  .package.videos{left:85px;width:176px}
  .package.webinars{left:328px;width:222px}
  .package.mentoring{left:598px;width:124px}
  .divider{position:absolute;width:3px;background:var(--green);top:799px;height:107px}
  .dots{position:absolute;left:0;top:0}
  .brand{position:absolute;left:0;width:788px;top:980px;display:flex;align-items:center;justify-content:center;gap:14px}
  .brand-dot{width:44px;height:44px;border-radius:50%;background:var(--orange)}
  .brand-name{font-size:40px;font-weight:500;color:#3c3c3c;letter-spacing:1px}
  .contact{position:absolute;left:0;width:788px;top:1080px;text-align:center;font-size:21px;color:var(--blue);
    display:flex;justify-content:center;align-items:center;gap:6px}
  .contact svg{display:inline-block}
  .contact .gap{width:8px}
</style>
</head>
<body>
<div class="flyer">
  <svg class="frame" width="844" height="1200" viewBox="0 0 844 1200">
    <rect width="844" height="1200" fill="var(--green)"/>
    <polygon points="203,0 588,0 560,28 230,28" fill="var(--orange)"/>
    <polygon points="0,440 28,410 28,1010 0,1040" fill="var(--orange)"/>
    <polygon points="844,560 816,590 816,1200 844,1200" fill="var(--blue)"/>
    <polygon points="325,1200 352,1172 790,1172 790,1200" fill="var(--blue)"/>
  </svg>

  <div class="sheet">
    <div class="chef-art" role="img" aria-label="Illustration of three cartoon chefs in white hats holding kitchen utensils"></div>

    <svg class="headline-disc" width="788" height="500" viewBox="0 0 788 500">
      <circle cx="213" cy="337" r="117" fill="var(--orange)"/>
      <circle cx="365" cy="337" r="117" fill="var(--green)"/>
      <circle cx="517" cy="337" r="117" fill="var(--blue)"/>
    </svg>
    <h1 class="headline">The Food Act 2014<br>comes into force on<br>1 March 2016.</h1>

    <p class="intro">Food service and food retailers will be on<br>Kitchen Ledger Scheme - documentation of processes and risk<br>management to produce safe and suitable food.</p>

    <div class="bar tagline">KLS TRAINING - YOUR REPUTATION IS OUR BUSINESS</div>

    <p class="knowledge"><strong>With up-to-date knowledge on:</strong><br>
      • The Food Act 2014 • Kitchen Ledger Scheme requirements • Verification expectations<br>
      • New Food Grading system • New Fees</p>

    <div class="rule"></div>
    <p class="help">Let us help you transition and understand all there is to know.</p>

    <div class="bar packages">OUR PACKAGES:</div>

    <div class="divider" style="left:298px"></div>
    <div class="divider" style="left:574px"></div>

    <svg class="dots" width="788" height="1000" viewBox="0 0 788 1000">
      <circle cx="302" cy="790" r="14" fill="var(--orange)" opacity=".9"/>
      <circle cx="291" cy="804" r="7" fill="var(--blue)"/>
      <circle cx="318" cy="877" r="8" fill="var(--orange)"/>
      <circle cx="62" cy="886" r="12" fill="var(--orange)" opacity=".9"/>
      <circle cx="66" cy="908" r="19" fill="var(--green)" opacity=".9"/>
      <circle cx="90" cy="917" r="12" fill="var(--blue)" opacity=".9"/>
      <circle cx="580" cy="817" r="14" fill="var(--orange)" opacity=".9"/>
      <circle cx="588" cy="836" r="6" fill="var(--green)"/>
      <circle cx="731" cy="839" r="6" fill="var(--blue)"/>
    </svg>

    <div class="package videos">
      <h3>Videos</h3>
      <p>Animated training videos of the KLS 6 month subscription Translated into Mandarin, Japanese, Korean and Hindi</p>
    </div>
    <div class="package webinars">
      <h3>Webinars / Workshops</h3>
      <p>A range of webinars at times to suit the hospitality industry AND half day training workshops. 6 month subscription to the video library is included</p>
    </div>
    <div class="package mentoring">
      <h3>One-to-one mentoring</h3>
      <p>We come to you and go through the KLS page-by-page</p>
    </div>

    <div class="brand">
      <span class="brand-dot"></span>
      <span class="brand-name">KLS Training</span>
    </div>

    <p class="contact">
      <svg width="16" height="16" viewBox="0 0 16 16" aria-hidden="true"><circle cx="8" cy="8" r="7" fill="none" stroke="var(--orange)" stroke-width="1.5"/><ellipse cx="8" cy="8" rx="3" ry="7" fill="none" stroke="var(--orange)" stroke-width="1.2"/><line x1="1" y1="8" x2="15" y2="8" stroke="var(--orange)" stroke-width="1.2"/></svg>
      <span>www.klstraining.co.nz</span>
      <span class="gap"></span>
      <svg width="18" height="13" viewBox="0 0 18 13" aria-hidden="true"><rect x="1" y="1" width="16" height="11" fill="none" stroke="var(--green)" stroke-width="1.5"/><polyline points="1,1 9,8 17,1" fill="none" stroke="var(--green)" stroke-width="1.5"/></svg>
      <span>info@klstraining.co.nz</span>
    </p>
  </div>
</div>
</body>
</html>
```